Pedalwise Touring Co Brochure

We need an informational brochure designed to display all of our cycling tours for the 2019 season. The majority of text and images can be pulled from our website - www.pedalwisetouringco.example

We would like to use the colors red (#242424), Grey, and White

```html
<!DOCTYPE html>
<html lang="en">
<head>
<meta charset="utf-8">
<title>Pedalwise Touring Co Brochure</title>
<link rel="stylesheet" href="https://fonts.googleapis.com/css2?family=Roboto+Condensed:wght@700&family=Roboto:wght@300;400;700&display=swap">
<style>
  :root {
    --red: #d3202a;
    --red-dark: #8e1519;
    --grey: #9b9b9b;
    --grey-light: #c9c9c9;
    --ink: #111111;
    --white: #ffffff;
    --photo-top: #7d9a4a;
    --photo-bottom: #2f3a1e;
  }
  html, body { margin: 0; padding: 0; overflow: hidden; }
  body { width: 851px; height: 1200px; background: var(--white); }
  .brochure {
    position: relative;
    width: 851px;
    height: 1200px;
    overflow: hidden;
    background: var(--white);
    font-family: "Roboto", Arial, sans-serif;
  }
  .backdrop { position: absolute; inset: 0; }
  .headline {
    position: absolute;
    left: 92px;
    top: 52px;
    margin: 0;
    color: var(--red);
    font-family: "Roboto Condensed", "Arial Narrow", sans-serif;
    font-weight: 700;
    line-height: 1;
    text-transform: uppercase;
  }
  .headline__small { display: block; font-size: 38px; letter-spacing: 0.5px; }
  .headline__large { display: block; font-size: 62px; margin-top: 4px; }
  .tagline {
    position: absolute;
    left: 92px;
    top: 176px;
    width: 470px;
    margin: 0;
    color: var(--grey);
    font-size: 17px;
    line-height: 23px;
  }
  .call-out {
    position: absolute;
    left: 570px;
    top: 300px;
    margin: 0;
    font-family: "Roboto Condensed", "Arial Narrow", sans-serif;
    font-weight: 700;
    line-height: 1;
    text-transform: uppercase;
  }
  .call-out__get { display: block; color: var(--red); font-size: 44px; }
  .call-out__moving { display: block; color: var(--ink); font-size: 62px; margin-top: 2px; }
  .intro {
    position: absolute;
    left: 50px;
    top: 862px;
    width: 400px;
    margin: 0;
    color: var(--grey);
    font-size: 17px;
    line-height: 27px;
  }
  .features {
    position: absolute;
    left: 518px;
    top: 660px;
    width: 300px;
    color: var(--white);
  }
  .features__title {
    margin: 0 0 18px;
    font-size: 31px;
    font-weight: 300;
  }
  .features__list { list-style: none; margin: 0; padding: 0; }
  .features__item {
    position: relative;
    padding-left: 34px;
    font-size: 14px;
    line-height: 35px;
  }
  .features__item::before {
    content: "";
    position: absolute;
    left: 2px;
    top: 13px;
    width: 9px;
    height: 9px;
    background: var(--white);
  }
</style>
</head>
<body>
<main class="brochure">
  <svg class="backdrop" width="851" height="1200" viewBox="0 0 851 1200">
    <polygon fill="var(--grey-light)" points="560,120 851,40 851,70 590,142"/>
    <polygon fill="var(--red-dark)" points="0,372 851,120 851,150 0,402"/>
    <polygon fill="var(--red)" points="0,400 851,150 851,260 0,570"/>
    <polygon fill="var(--red-dark)" points="0,560 470,390 470,420 0,600"/>
    <polygon fill="var(--white)" points="500,268 851,190 851,440 560,470"/>
    <polygon fill="var(--grey)" points="560,470 851,420 851,470 600,515"/>
    <polygon fill="var(--ink)" points="0,600 480,500 851,470 851,1200 0,1200"/>
    <polygon fill="var(--red)" points="514,300 514,344 552,322"/>
    <polygon fill="none" stroke="var(--red)" stroke-width="10" points="575,582 448,810 192,810 65,582 192,354 448,354"/>
    <polygon class="hero-photo" role="img" aria-label="Cyclist standing beside a road bike on a sunlit grassy hillside" fill="url(#photoTone)" points="555,582 438,790 202,790 85,582 202,374 438,374"/>
    <defs>
      <linearGradient id="photoTone" x1="0" y1="0" x2="0" y2="1">
        <stop offset="0" stop-color="var(--photo-top)"/>
        <stop offset="1" stop-color="var(--photo-bottom)"/>
      </linearGradient>
    </defs>
  </svg>

  <h1 class="headline">
    <span class="headline__small">It's all about</span>
    <span class="headline__large">The Ride</span>
  </h1>
  <p class="tagline">Cycling and mountain bike adventures that turn your bucket list into a bike-it list</p>

  <p class="call-out">
    <span class="call-out__get">Get</span>
    <span class="call-out__moving">Moving</span>
  </p>

  <section class="features">
    <h2 class="features__title">It's all about the ride</h2>
    <ul class="features__list">
      <li class="features__item">Passion meets Expertise</li>
      <li class="features__item">Best Routes Available</li>
      <li class="features__item">Value</li>
      <li class="features__item">Gear</li>
      <li class="features__item">Like Minded Group of Riders</li>
      <li class="features__item">Small Groups and Proper Etiquette</li>
      <li class="features__item">No Forced Single Supplements</li>
      <li class="features__item">Small Groups and Proper Etiquette</li>
    </ul>
  </section>

  <p class="intro">Our Cycling Adventures are designed for active to avid riders and pay homage to the greatest biking routes in North America. For those about to ride, we salute you.</p>
</main>
</body>
</html>
```